Web Design Project for Torvalia cloud based service

None of us is a designer, and ENGLISH is not our first language, but we need to make sure that those bidding for this project understand that we're just looking for the creative components in order to build a website and we don't need you to create all the pages and /or diagram the website for us. Please ask as many questions as you want for us to ensure we don't waste your time.

Content and Community Management System
- We need a redesign of the Back Office Screens
o The kind of screen detailed on the (file 2 attached bellow) “Torvalia Some Screens.pptx”
- Following, as a strong reference te torvalia logo design line (file 1 attached bellow)
- We DO NOT need application, or implementation, only the following SOW.

Scope of Work (SOW) by components that we need:
- Main Theme
- Tables
- Buttons
- Icons
- Lists
- Form elements

OUT of Scope (we DO NOT need it):
· Emerging Windows implementation (jquery – lightbox)
· Layout (we do not need you to create the layout for us)
· Module Development (Css 3, jQuery, Html 5)

Project Deadline Extended
Reason: We're extending the deadline in order to have more options to select. The current option do not fit our expectation yet. Any question, please do it. Many thanks. Torvalia Team.

Hi designers!

We've [a] extended the deadline in order to have more choices and we made a change on the Power Point file attached with [b] the 3 most important screen than include all the components/element we need designed from you.

We wait for your proposal.
Let's do it!

Many Thanks.
Best regards.

torvalia Team.

```html
<!DOCTYPE html>
<html lang="es">
<head>
<meta charset="utf-8">
<title>Torvalia – Back Office</title>
<link rel="stylesheet" href="https://fonts.googleapis.com/css2?family=Source+Sans+3:wght@400;600&display=swap">
<style>
  :root {
    --page-bg: #ebebeb;
    --glow: #ffffff;
    --panel: #ffffff;
    --bar: #dcdcdc;
    --accent: #e84c0a;
    --green: #4f9a16;
    --text: #3a3a3a;
    --body-text: #505050;
    --muted: #555555;
    --rule: #d9d9d9;
    --link-bg: #ebebeb;
  }
  * { box-sizing: border-box; margin: 0; padding: 0; }
  html, body { width: 1200px; height: 752px; overflow: hidden; }
  body {
    position: relative;
    font-family: "Source Sans 3", "Myriad Pro", sans-serif;
    color: var(--text);
    background:
      radial-gradient(circle at 135px 110px, var(--glow) 0, var(--glow) 90px, rgba(255,255,255,0) 190px),
      var(--page-bg);
  }

  .brand { position: absolute; left: 67px; top: 48px; display: flex; flex-direction: column; align-items: flex-start; gap: 12px; }
  .brand-mark { width: 88px; height: 88px; background: var(--accent); }
  .brand-name { font-size: 27px; font-weight: 600; color: #1e1e1e; letter-spacing: 0.5px; line-height: 1; }

  .main-nav { position: absolute; top: 129px; left: 329px; height: 37px; width: 820px; }
  .main-nav a {
    position: absolute; top: 0; height: 37px; line-height: 37px;
    font-size: 15px; color: #3d3d3d; text-decoration: none; text-align: center;
    white-space: nowrap;
    transform: translateX(-50%);
  }
  .main-nav a.is-active { background: var(--accent); color: #fff; width: 134px; transform: none; }

  .context-bar {
    position: absolute; left: 35px; top: 211px; width: 1125px; height: 50px;
    background: var(--bar);
  }
  .context-title { position: absolute; left: 28px; top: 13px; font-size: 17px; color: #444; }
  .user-links { position: absolute; right: 44px; top: 16px; font-size: 14px; color: var(--muted); white-space: nowrap; }
  .user-links span.sep { margin: 0 6px; }

  .content-panel { position: absolute; left: 35px; top: 261px; width: 1123px; height: 491px; background: var(--panel); }

  .section-title { position: absolute; left: 29px; top: 32px; font-size: 21px; font-weight: 400; color: #2a2a2a; }
  .section-rule {
    position: absolute; left: 29px; top: 66px; width: 487px; height: 1px;
    background: linear-gradient(to right, #cfcfcf, rgba(207,207,207,0));
  }

  .feature { position: absolute; width: 260px; }
  .feature h2 { font-size: 18px; font-weight: 400; color: var(--green); line-height: 1.2; margin-bottom: 3px; white-space: nowrap; }
  .feature p { font-size: 13px; line-height: 17.5px; color: var(--body-text); white-space: nowrap; }
  .col-divider { position: absolute; width: 1px; background: var(--rule); top: 102px; height: 256px; }
  .row-divider { position: absolute; left: 27px; top: 223px; width: 812px; height: 1px; background: var(--rule); }

  .goto { position: absolute; left: 891px; top: 42px; width: 210px; }
  .goto-title { font-size: 21px; font-weight: 400; color: #2a2a2a; margin-left: 1px; margin-bottom: 10px; }
  .goto-list { list-style: none; }
  .goto-list li {
    height: 23px; margin-bottom: 2.8px; background: var(--link-bg);
    font-size: 12.5px; line-height: 23px; color: #333; padding-left: 36px; position: relative; white-space: nowrap;
  }
  .goto-list li svg { position: absolute; left: 17px; top: 7px; }
</style>
</head>
<body>

  <div class="brand">
    <div class="brand-mark"></div>
    <div class="brand-name">TORVALIA</div>
  </div>

  <nav class="main-nav">
    <a class="is-active" href="#" style="left:0">Company</a>
    <a href="#" style="left:197px">About Us</a>
    <a href="#" style="left:336px">Testimonials</a>
    <a href="#" style="left:474px">Modules</a>
    <a href="#" style="left:617px">Adminstrative</a>
    <a href="#" style="left:763px">Live Store</a>
  </nav>

  <header class="context-bar">
    <div class="context-title">Proyecto:Region: BRASIL</div>
    <div class="user-links">User admin <span class="sep">|</span>Profeceinces<span class="sep">|</span>Profile<span class="sep">|</span>Siler</div>
  </header>

  <main class="content-panel">
    <h1 class="section-title">Secciones Principales</h1>
    <div class="section-rule"></div>

    <div class="col-divider" style="left:287px"></div>
    <div class="col-divider" style="left:576px"></div>
    <div class="col-divider" style="left:287px; top:224px; height:134px"></div>
    <div class="row-divider"></div>

    <article class="feature" style="left:28px; top:96px">
      <h2>Heading First</h2>
      <p>Static website is a simple way to get your<br>message out to the public. Static website<br>are cheaper and also it needs less main-<br>tenance too. It’s the simplest, cheapest</p>
    </article>
    <article class="feature" style="left:313px; top:101px">
      <h2>Heading First</h2>
      <p>Static website is a simple way to get your<br>message out to the public. Static website<br>are cheaper and also it needs less mainte-<br>nance too. It’s the simplest, cheapest</p>
    </article>
    <article class="feature" style="left:598px; top:95px">
      <h2>Heading First</h2>
      <p>Static website is a simple way to get your<br>message out to the public. Static website<br>are cheaper and also it needs less mainte-<br>nance too. It’s the simplest, cheapest</p>
    </article>

    <article class="feature" style="left:26px; top:246px">
      <h2>Heading First</h2>
      <p>Static website is a simple way to get your<br>message out to the public. Static website<br>are cheaper and also it needs less mainte-<br>nance too. It’s the simplest, cheapest</p>
    </article>
    <article class="feature" style="left:313px; top:245px">
      <h2>Heading First</h2>
      <p>Static website is a simple way to get your<br>message out to the public. Static website<br>are cheaper and also it needs less mainte-<br>nance too. It’s the simplest, cheapest</p>
    </article>
    <article class="feature" style="left:600px; top:245px">
      <h2>Heading First</h2>
      <p>Static website is a simple way to get your<br>message out to the public. Static website<br>are cheaper and also it needs less main-<br>tenance too. It’s the simplest, cheapest</p>
    </article>

    <aside class="goto">
      <h2 class="goto-title">Ir a:</h2>
      <ul class="goto-list">
        <li><svg width="8" height="9" viewBox="0 0 8 9"><path d="M0 0 L8 4.5 L0 9 Z" fill="#4f9a16"/></svg>Your heading goes here</li>
        <li><svg width="8" height="9" viewBox="0 0 8 9"><path d="M0 0 L8 4.5 L0 9 Z" fill="#4f9a16"/></svg>heading goes here</li>
        <li><svg width="8" height="9" viewBox="0 0 8 9"><path d="M0 0 L8 4.5 L0 9 Z" fill="#4f9a16"/></svg>Your heading goes here</li>
        <li><svg width="8" height="9" viewBox="0 0 8 9"><path d="M0 0 L8 4.5 L0 9 Z" fill="#4f9a16"/></svg>heading goes here</li>
        <li><svg width="8" height="9" viewBox="0 0 8 9"><path d="M0 0 L8 4.5 L0 9 Z" fill="#4f9a16"/></svg>Your heading goes here</li>
        <li><svg width="8" height="9" viewBox="0 0 8 9"><path d="M0 0 L8 4.5 L0 9 Z" fill="#4f9a16"/></svg>heading goes here</li>
        <li><svg width="8" height="9" viewBox="0 0 8 9"><path d="M0 0 L8 4.5 L0 9 Z" fill="#4f9a16"/></svg>Your heading goes here</li>
        <li><svg width="8" height="9" viewBox="0 0 8 9"><path d="M0 0 L8 4.5 L0 9 Z" fill="#4f9a16"/></svg>heading goes here</li>
        <li><svg width="8" height="9" viewBox="0 0 8 9"><path d="M0 0 L8 4.5 L0 9 Z" fill="#4f9a16"/></svg>Your heading goes here</li>
        <li><svg width="8" height="9" viewBox="0 0 8 9"><path d="M0 0 L8 4.5 L0 9 Z" fill="#4f9a16"/></svg>heading goes here</li>
        <li><svg width="8" height="9" viewBox="0 0 8 9"><path d="M0 0 L8 4.5 L0 9 Z" fill="#4f9a16"/></svg>Your heading goes here</li>
        <li><svg width="8" height="9" viewBox="0 0 8 9"><path d="M0 0 L8 4.5 L0 9 Z" fill="#4f9a16"/></svg>heading goes here</li>
      </ul>
    </aside>
  </main>

</body>
</html>
```